Business Card Design

I want to pull elements/colors from Website. Attached is a screen shot. Do not want any buildings/building graphics/construction clichés. This is for a construction management firm but I want to keep it broad enough that I can expand into other areas. I do not want the logo to be limited. Thank you.
Updates

Please review the screen shot of the website. Please use the font and color of Brackwell Holdings, LLC on the website. Please use the tag line "Construction Management in the Palm Beaches" Please show contractor license ... CGC 7390462 You may use the back for the contact information. Please no phone/house icons. It does not have to be a black card. Thank you.

Target Market(s)

Professional people with money. Owners, Architects, Engineers, Developers, Real Estate Agents etc.

Industry/Entity Type

Construction

Contact Information for Business Card

Brackwell Holdings, LLC
Construction Management

Dean T Brackwell
418 Ostrander Court #73
North Palm Beach, FL 33412
(561) 555-0187
www.BrackwellHoldings.example

Requirements
Must have
• Clean, crisp, modern.

Broad enough that it is not trapped into a particular industry.

My goal is to expand into different markets, different industries.

Should not have
• The back of the card should not be colored in any way. Rubs off on other cards.

Do not want any buildings/building graphics/construction clichés.

```html
<!DOCTYPE html>
<html lang="en">
<head>
<meta charset="utf-8">
<title>Brackwell Holdings – Business Card</title>
<link rel="stylesheet" href="https://fonts.googleapis.com/css2?family=Exo+2:wght@300;400;500;600&display=swap">
<style>
  :root {
    --backdrop: #6c6e75;
    --card-white: #ffffff;
    --brand-blue: #1ba8e0;
    --brand-blue-deep: #168fc2;
    --panel-grey: #ebebec;
    --band-grey: #58595b;
    --accent-teal: #3a7f9c;
    --ink-dark: #2b2c2e;
    --ink-grey: #6d6e70;
  }
  html, body {
    margin: 0;
    padding: 0;
    width: 1200px;
    height: 1082px;
    overflow: hidden;
    background: var(--backdrop);
    font-family: "Exo 2", sans-serif;
  }
  .card {
    position: absolute;
    left: 75px;
    top: 241px;
    width: 1050px;
    height: 600px;
    background: var(--card-white);
    overflow: hidden;
    box-shadow: 0 10px 30px rgba(0,0,0,0.25);
  }
  .card-shapes {
    position: absolute;
    inset: 0;
  }
  .name-line {
    position: absolute;
    left: 400px;
    top: 56px;
    margin: 0;
    font-size: 30px;
    font-weight: 500;
    letter-spacing: 2px;
    color: var(--ink-dark);
    text-transform: uppercase;
    white-space: nowrap;
  }
  .name-line .divider {
    margin: 0 18px;
    font-weight: 400;
  }
  .name-line .role {
    font-size: 22px;
    font-weight: 400;
    letter-spacing: 2px;
  }
  .brand {
    position: absolute;
    left: 500px;
    top: 195px;
  }
  .brand-name {
    margin: 0;
    font-size: 74px;
    line-height: 1;
    font-weight: 500;
    color: var(--brand-blue);
  }
  .brand-sub {
    margin: 6px 0 0 70px;
    font-size: 40px;
    line-height: 1;
    font-weight: 300;
    letter-spacing: 6px;
    color: var(--ink-grey);
  }
  .tagline {
    margin: 18px 0 0 0;
    font-size: 18px;
    line-height: 1.2;
    font-weight: 400;
    letter-spacing: 1px;
    color: var(--ink-dark);
    white-space: nowrap;
  }
  .contact-list {
    position: absolute;
    left: 40px;
    top: 205px;
    margin: 0;
    padding: 0;
    list-style: none;
    font-size: 17px;
    color: var(--ink-dark);
  }
  .contact-list li {
    display: flex;
    align-items: center;
    gap: 12px;
    height: 34px;
    white-space: nowrap;
  }
  .contact-list .label {
    width: 16px;
    flex: none;
    font-weight: 600;
    color: var(--brand-blue);
  }
  .address {
    position: absolute;
    right: 40px;
    top: 495px;
    margin: 0;
    font-size: 24px;
    font-weight: 400;
    letter-spacing: 1px;
    color: #ffffff;
    white-space: nowrap;
  }
</style>
</head>
<body>
  <main class="card">
    <svg class="card-shapes" viewBox="0 0 1050 600" width="1050" height="600" aria-hidden="true">
      <rect class="top-band" x="0" y="0" width="1050" height="160" fill="var(--brand-blue)"/>
      <polygon class="top-band-shade" points="0,0 250,0 360,160 0,160" fill="var(--brand-blue-deep)" opacity="0.45"/>
      <rect class="contact-panel" x="0" y="160" width="360" height="280" fill="var(--panel-grey)"/>
      <polygon class="bottom-band" points="330,440 1050,440 1050,600 300,600" fill="var(--band-grey)"/>
      <polygon class="bottom-accent" points="300,600 330,440 620,440" fill="var(--accent-teal)"/>
    </svg>

    <h1 class="name-line">Dean T Brackwell<span class="divider">|</span><span class="role">General Manager</span></h1>

    <div class="brand">
      <p class="brand-name">Brackwell</p>
      <p class="brand-sub">Holdings</p>
      <p class="tagline">Construction Management in the Palm Beaches</p>
    </div>

    <ul class="contact-list">
      <li><span class="label">T</span><span>(561) 555-0187</span></li>
      <li><span class="label">M</span><span>(561) 555-0187</span></li>
      <li><span class="label">F</span><span>(561) 555-0187</span></li>
      <li><span class="label">E</span><span>dean@brackwellholdings.example</span></li>
      <li><span class="label">W</span><span>www.BrackwellHoldings.example</span></li>
      <li><span class="label">L</span><span>CGC 7390462</span></li>
    </ul>

    <p class="address">418 Ostrander Court #73, North Palm Beach, FL 33412</p>
  </main>
</body>
</html>
```